Ripple (nightclub flyer)

Nightclub flyer, guaranteed project. Text below (and please use logos, large):

RIPPLE PRESENTS:

KORVEN (LOGO) B2B MARTIN VOLKE (LOGO)

+TREVV LANE (smaller text)

10/26/17

2284 HARLOW AVENUE SACRAMENTO CA
21+ 10PM-2AM

HOUSE/TECHNO

A BLUE CASCADE ENTERTAINMENT (LOGO) PRODUCTION

Target Market(s)

House/Electronic Music Lovers

Industry/Entity Type

Night Club

Font styles to use
Sans Serif

Colors

Designer to choose colors to be used in the design.

Requirements
Must have
• Large logos for the dj names, or large block letter dj names (logos not necessary if it looks better without. But KORVEN b2b MARTIN VOLKE large and TREVV LANE smaller on separate line
Nice to have
• Can include a classy female model but nothing cheesy or too sexy

```html
<!DOCTYPE html>
<html lang="en">
<head>
<meta charset="utf-8">
<title>Ripple Presents: Korven B2B Martin Volke</title>
<link rel="stylesheet" href="https://fonts.googleapis.com/css2?family=Arimo:ital,wght@0,400;0,700;1,400;1,700&display=swap">
<style>
  :root {
    --page-bg: #e9ecef;
    --flyer-deep: #1f4a63;
    --flyer-mid: #3f7c9a;
    --flyer-light: #6fa6c0;
    --band-light: #d7dde2;
    --band-dark: #7a858e;
    --text-white: #ffffff;
    --text-dark: #2a3238;
    --logo-blue: #2f4fa3;
    --badge-dark: #1d3340;
  }
  * { box-sizing: border-box; margin: 0; padding: 0; }
  html, body { width: 1200px; height: 1000px; overflow: hidden; }
  body {
    background: var(--page-bg);
    font-family: "Arimo", Arial, sans-serif;
    position: relative;
  }
  .flyer {
    position: absolute;
    left: 50px; top: 280px;
    width: 1100px; height: 440px;
    overflow: hidden;
    background: linear-gradient(160deg, var(--flyer-light) 0%, var(--flyer-mid) 45%, var(--flyer-deep) 100%);
    box-shadow: 0 8px 24px rgba(0,0,0,0.25);
  }
  .model-photo {
    position: absolute;
    left: 560px; top: 0;
    width: 540px; height: 440px;
    background: radial-gradient(ellipse at 55% 45%, #8bb7cc 0%, #5a93ae 40%, #2e627c 75%, #1f4a63 100%);
    opacity: 0.9;
  }
  .title-band {
    position: absolute;
    left: 0; top: 20px;
    width: 490px; height: 120px;
    background: linear-gradient(180deg, var(--band-light) 0%, var(--band-dark) 100%);
    clip-path: polygon(0 0, 100% 0, 90% 100%, 0 100%);
    opacity: 0.85;
  }
  .promoter {
    position: absolute;
    left: 40px; top: 28px;
    font: italic 700 72px/1 "Arimo", Arial, sans-serif;
    color: var(--text-white);
    letter-spacing: 1px;
  }
  .presents {
    position: absolute;
    left: 40px; top: 102px;
    font: italic 400 30px/1 "Arimo", Arial, sans-serif;
    color: var(--text-dark);
  }
  .badges { position: absolute; left: 0; top: 0; }
  .korven-mark {
    position: absolute;
    left: 10px; top: 228px;
    width: 200px;
    text-align: center;
    font: 700 32px/1 "Arimo", Arial, sans-serif;
    color: var(--logo-blue);
  }
  .volke-mark {
    position: absolute;
    left: 87px; top: 370px;
    width: 150px;
    text-align: center;
    font: 400 14px/1 "Arimo", Arial, sans-serif;
    color: var(--text-white);
  }
  .headliner, .b2b, .partner, .support {
    position: absolute;
    color: var(--text-white);
    font-style: italic;
    font-weight: 700;
    line-height: 1;
  }
  .headliner { left: 215px; top: 192px; font-size: 56px; }
  .b2b { left: 262px; top: 264px; font-size: 52px; }
  .partner { left: 262px; top: 318px; font-size: 40px; }
  .support { left: 262px; top: 382px; font-size: 26px; }
  .event-details {
    position: absolute;
    right: 28px; bottom: 28px;
    text-align: right;
    color: var(--text-white);
    font-weight: 700;
    line-height: 1.15;
  }
  .event-date { font-size: 36px; }
  .event-venue { font-size: 16px; }
  .event-entry { font-size: 24px; }
  .event-genre { font-size: 28px; margin-top: 6px; }
</style>
</head>
<body>
  <div class="flyer">
    <div class="model-photo" role="img" aria-label="Photo of a female model tinted in cool blue tones"></div>
    <div class="title-band"></div>
    <div class="promoter">RIPPLE</div>
    <div class="presents">PRESENTS:</div>

    <svg class="badges" width="560" height="440" viewBox="0 0 560 440" aria-hidden="true">
      <circle cx="110" cy="245" r="90" fill="rgba(255,255,255,0.08)" stroke="#3c4fa0" stroke-width="2"/>
      <circle cx="162" cy="355" r="75" fill="#4d7a92" stroke="#a9c3d1" stroke-width="2"/>
      <circle cx="162" cy="337" r="22" fill="var(--badge-dark)"/>
    </svg>
    <div class="korven-mark">KORVEN</div>
    <div class="volke-mark">MARTIN VOLKE</div>

    <div class="headliner">KORVEN</div>
    <div class="b2b">B2B</div>
    <div class="partner">MARTIN VOLKE</div>
    <div class="support">+ TREVV LANE</div>

    <div class="event-details">
      <div class="event-date">10/26/17</div>
      <div class="event-venue">2284 HARLOW AVENUE SACRAMENTO CA</div>
      <div class="event-entry">21+ 10PM-2AM</div>
      <div class="event-genre">HOUSE / TECHNO</div>
    </div>
  </div>
</body>
</html>
```